Lotzy Template Design in Baby Category

We are a maternity/baby store on Lotzy in need of a store front design template (Store front, listing and detail page page) that is accustom to our category, is user friendly, easy to read and navigate and mobile friendly.

The design should be reflecting a motherhood warm feeling with a modern look.

Please don't hesitate to inquire, if you need any clarification.

Thank you

Baby

3 page

```html
<!DOCTYPE html>
<html lang="en">
<head>
<meta charset="utf-8">
<title>Mama Nest – Lotzy Store Front</title>
<link rel="stylesheet" href="https://fonts.googleapis.com/css2?family=Open+Sans:wght@400;600;700&family=Oswald:wght@400;500&family=Dancing+Script:wght@600&display=swap">
<style>
:root{
  --purple:#7a5ca6;
  --purple-light:#9a80c2;
  --dark:#3b3b3d;
  --panel:#e9e9ea;
  --line:#d6d6d8;
  --text:#555;
  --muted:#888;
  --price:#b0407a;
  --gold:#e6b53a;
  --white:#fff;
}
*{box-sizing:border-box;margin:0;padding:0}
html,body{width:831px;height:1200px;overflow:hidden;background:var(--white);font-family:"Open Sans",Arial,sans-serif;color:var(--text)}
.page{position:relative;width:563px;margin:0 auto;height:1200px}
.topbar{height:19px;background:var(--purple);display:flex;justify-content:flex-end;align-items:center;gap:14px;padding-right:10px;font-size:6.5px;font-weight:700;color:var(--white);letter-spacing:.3px}
.header{height:66px;display:flex;justify-content:space-between;align-items:center;padding:0 10px}
.brand{display:flex;align-items:center;gap:8px}
.brand-dot{width:26px;height:26px;border-radius:50%;background:var(--purple-light)}
.brand-name{font-family:"Dancing Script",cursive;font-size:22px;color:var(--dark);font-weight:600}
.contact{list-style:none;font-size:7px;color:var(--dark)}
.contact li{display:flex;align-items:center;gap:5px;margin:3px 0}
.contact .ico{width:11px;height:11px;background:var(--purple);display:flex;align-items:center;justify-content:center}
.nav{height:34px;background:var(--dark);display:flex;align-items:center;padding:0 8px;gap:16px;font-size:7px;font-weight:700;color:var(--white)}
.nav .home{width:20px;height:34px;display:flex;align-items:center;justify-content:center;background:#2b2b2c}
.search{margin-left:auto;width:112px;height:16px;background:var(--white);display:flex;align-items:center;justify-content:space-between;padding:0 4px;font-size:6px;font-weight:400;color:var(--muted)}
.body{display:flex;gap:10px;padding:8px 6px 0}
.sidebar{width:126px}
.box{background:var(--panel);margin-bottom:10px;padding-bottom:8px}
.box h3{background:var(--purple);color:var(--white);font-size:7px;font-weight:700;padding:5px 7px;letter-spacing:.3px}
.cats{list-style:none;padding:4px 6px 0}
.cats li{font-size:6.5px;padding:5px 4px;border-bottom:1px solid var(--line);color:var(--text)}
.cats li.active{background:var(--white);color:var(--purple);font-weight:600}
.pay{display:flex;flex-direction:column;align-items:center;padding-top:10px;gap:7px}
.pay .seal{width:46px;height:46px;border-radius:50%;background:var(--gold)}
.cards{display:grid;grid-template-columns:repeat(3,22px);gap:4px}
.cards span{height:13px;background:#cfd3da;border-radius:2px}
.social{display:flex;gap:5px;padding:10px 7px 2px}
.social span{width:20px;height:20px;border-radius:3px}
.main{flex:1}
.banner{height:125px;background:#ededee;display:flex;align-items:center;padding:0 14px;justify-content:space-between}
.banner-text{margin-left:60px;text-align:right}
.banner h1{font-family:"Oswald",sans-serif;font-weight:500;font-size:26px;color:var(--dark);letter-spacing:1px;line-height:1}
.banner p{font-size:6px;color:var(--purple);letter-spacing:.5px;margin-top:3px;line-height:1.4}
.banner-photo{width:150px;height:100px;background:linear-gradient(135deg,#d9a766,#f3e2c6 60%,#fafafa)}
.sortbar{height:20px;background:var(--dark);margin-top:11px;display:flex;align-items:center;padding:0 8px;gap:30px;font-size:5.5px;color:#ddd;font-weight:600}
.sortbar .view{margin-left:auto}
.product{display:flex;height:150px;margin-top:10px;border-bottom:1px solid #eee}
.product-photo{width:110px;height:148px;border:1px solid #eee;padding:8px 14px}
.product-photo div{width:100%;height:100%}
.p-info{display:flex;flex:1;padding:28px 0 0 16px;font-size:7px;gap:20px}
.p-title{width:120px;color:var(--dark);line-height:1.4}
.p-sale{width:70px;color:var(--muted)}
.p-price{margin-left:auto;text-align:right;color:var(--price);font-weight:600}
.p-price small{display:block;font-size:5.5px;color:var(--purple);font-weight:700;margin-top:2px}
.pager{height:20px;background:var(--dark);margin-top:20px;display:flex;justify-content:center;align-items:center;gap:6px;font-size:6px;color:#ddd;font-weight:600}
.footer{position:absolute;bottom:10px;left:0;right:0;text-align:center;font-size:6px;color:var(--purple)}
</style>
</head>
<body>
<div class="page">
  <div class="topbar"><span>SALE</span><span>AUCTIONS</span><span>BROWSE STORE</span><span>NEWSLETTER</span></div>

  <header class="header">
    <div class="brand"><span class="brand-dot"></span><span class="brand-name">Mama Nest</span></div>
    <ul class="contact">
      <li><span class="ico"><svg width="7" height="7" viewBox="0 0 10 10"><path d="M2 1h2l1 2-1 1a5 5 0 0 0 2 2l1-1 2 1v2c-4 1-8-3-7-7z" fill="#fff"/></svg></span>(212) 555-0184</li>
      <li><span class="ico"><svg width="7" height="7" viewBox="0 0 10 10"><rect x="1" y="2" width="8" height="6" fill="none" stroke="#fff"/><path d="M1 2l4 3 4-3" fill="none" stroke="#fff"/></svg></span>info@mamanest.com</li>
      <li><span class="ico"><svg width="7" height="7" viewBox="0 0 10 10"><circle cx="5" cy="5" r="4" fill="none" stroke="#fff"/><path d="M1 5h8M5 1v8" stroke="#fff"/></svg></span>www.mamanest.com</li>
    </ul>
  </header>

  <nav class="nav">
    <span class="home"><svg width="10" height="10" viewBox="0 0 10 10"><path d="M1 5l4-4 4 4H8v4H6V6H4v3H2V5z" fill="#fff"/></svg></span>
    <span>ABOUT US</span><span>PAYMENT</span><span>SHIPPING</span><span>TERMS</span><span>CONTACT US</span><span>OUR STORE</span>
    <span class="search">Search keywords<svg width="7" height="7" viewBox="0 0 10 10"><circle cx="4" cy="4" r="3" fill="none" stroke="#555" stroke-width="1.5"/><path d="M6 6l3 3" stroke="#555" stroke-width="1.5"/></svg></span>
  </nav>

  <div class="body">
    <aside class="sidebar">
      <section class="box">
        <h3>CATEGORIES</h3>
        <ul class="cats">
          <li class="active">Nightwear</li><li>Nursing Tops</li><li>Supplements</li><li>Clothing</li><li>Baby Care</li><li>Skincare</li><li>Bedding</li><li>Maternity</li><li>Nursing Covers</li><li>Clothing Sets</li><li>Baby Gear</li><li>Vitamins</li><li>Belly Care</li><li>Others</li>
        </ul>
      </section>
      <section class="box">
        <h3>PAYMENT</h3>
        <div class="pay">
          <span class="seal"></span>
          <div class="cards"><span></span><span></span><span></span><span></span><span></span><span></span></div>
        </div>
      </section>
      <section class="box">
        <h3>CONNECT WITH US</h3>
        <div class="social"><span style="background:#3b5a98"></span><span style="background:#3aa3d9"></span><span style="background:#d0453a"></span><span style="background:#3f729b"></span></div>
      </section>
    </aside>

    <main class="main">
      <div class="banner">
        <div class="banner-text"><h1>PRODUCTS</h1><p>GENTLE CARE FOR EVERY MOM<br>SOFT SKIN DAY AND NIGHT</p></div>
        <div class="banner-photo" role="img" aria-label="Body balm jars and bottle product photo"></div>
      </div>
      <div class="sortbar"><span>10 PRODUCTS FOUND IN THIS STORE</span><span>SORT BY: BEST MATCH</span><span class="view">VIEW: LIST | GALLERY</span></div>

      <div class="product"><div class="product-photo"><div role="img" aria-label="Black and white patterned nursing cover" style="background:linear-gradient(180deg,#555,#999 50%,#444)"></div></div>
        <div class="p-info"><span class="p-title">Lullamoss Organics - Soft Bloom Body Balm</span><span class="p-sale">On Sale</span><span class="p-price">$19.99<small>FREE SHIPPING</small></span></div></div>
      <div class="product"><div class="product-photo"><div role="img" aria-label="Dark floral nursing cover" style="background:linear-gradient(180deg,#2d2d33,#4c3b4a 50%,#222)"></div></div>
        <div class="p-info"><span class="p-title">Lullamoss Organics - Soft Bloom Body Balm</span><span class="p-sale">On Sale</span><span class="p-price">$19.99<small>FREE SHIPPING</small></span></div></div>
      <div class="product"><div class="product-photo"><div role="img" aria-label="Pink and black floral nursing cover" style="background:linear-gradient(180deg,#4a3344,#c07a9e 50%,#3a2a35)"></div></div>
        <div class="p-info"><span class="p-title">Lullamoss Organics - Soft Bloom Body Balm</span><span class="p-sale">On Sale</span><span class="p-price">$19.99<small>FREE SHIPPING</small></span></div></div>
      <div class="product"><div class="product-photo"><div role="img" aria-label="Dark patterned nursing cover" style="background:linear-gradient(180deg,#26262b,#524a55 50%,#1f1f22)"></div></div>
        <div class="p-info"><span class="p-title">Lullamoss Organics - Soft Bloom Body Balm</span><span class="p-sale">On Sale</span><span class="p-price">$19.99<small>FREE SHIPPING</small></span></div></div>
      <div class="product"><div class="product-photo"><div role="img" aria-label="Light paisley nursing cover" style="background:linear-gradient(180deg,#d7c3b5,#b89b8e 50%,#e6d8cc)"></div></div>
        <div class="p-info"><span class="p-title">Lullamoss Organics - Soft Bloom Body Balm</span><span class="p-sale">On Sale</span><span class="p-price">$19.99<small>FREE SHIPPING</small></span></div></div>

      <div class="pager"><span>« PREVIOUS</span><span>1</span><span>2</span><span>3</span><span>4</span><span>5</span><span>6</span><span>NEXT »</span></div>
    </main>
  </div>

  <footer class="footer">© 2013 Mama Nest – New York, USA</footer>
</div>
</body>
</html>
```